Stationery Required - Own Logo provided

Hi,

We are a retail company called 'Copperfinch Trading Limited' based in the UK and would like some corporate stationery designed.

We have provided our Logo which we would like to use (Its attached to this brief)...

The designs must be orginal, professional, stylish and interesting!

Target Market(s)

We will use this stationery to communicate with our wholesale suppliers and employees, so it must have a 'professional' feel about it.

Industry/Entity Type

It Company

Requirements
Must have
• Must be professional, corporate, stylish and not to 'fussy'. we require ... Business card design, a4 letter, compliment slip. All designs must be supplied in a format where the text (address/telephone numbers etc..) can be edited, as we have alot of staff and operate out of several different premises.
Nice to have
• I would like a windows backround picture file supplied as well so we can integrate that onto our computer systems.

```html
<!DOCTYPE html>
<html lang="en">
<head>
<meta charset="utf-8">
<title>Copperfinch Trading Limited – Stationery</title>
<link rel="stylesheet" href="https://fonts.googleapis.com/css2?family=Source+Sans+3:wght@400;600&display=swap">
<style>
  :root {
    --backdrop: #4a4a4a;
    --leaf: #8dc63f;
    --forest: #3b5323;
    --paper: #ffffff;
    --ink: #333333;
    --ghost: #f1f2ee;
    --mist-1: #f6f9ef;
    --mist-2: #d9eabf;
  }
  * { box-sizing: border-box; margin: 0; padding: 0; }
  html, body {
    width: 1200px; height: 1200px; overflow: hidden;
    background: var(--backdrop);
    font-family: "Source Sans 3", "Myriad Pro", Arial, sans-serif;
    color: var(--ink);
  }
  .canvas { position: relative; width: 1200px; height: 1200px; }
  .sheet { position: absolute; background: var(--paper); overflow: hidden; }

  .wordmark {
    color: var(--leaf);
    font-weight: 600;
    line-height: 1;
    white-space: nowrap;
    display: flex; align-items: center; gap: 6px;
  }
  .wordmark .mark-square { width: 10px; height: 10px; background: var(--leaf); flex: none; }

  .contact { color: var(--ink); line-height: 1.45; text-align: center; }

  /* Business card */
  .business-card { left: 187px; top: 117px; width: 224px; height: 134px; }
  .business-card .top-band { position: absolute; left: 0; top: 0; width: 100%; height: 16px; background: var(--forest); }
  .business-card .wordmark { position: absolute; left: 0; right: 0; top: 36px; justify-content: center; font-size: 15px; }
  .business-card .person { position: absolute; left: 0; right: 0; top: 56px; text-align: center; }
  .business-card .person-name { font-size: 10px; color: var(--ink); }
  .business-card .person-role { font-size: 7px; color: var(--ink); }
  .business-card .contact-band {
    position: absolute; left: 0; bottom: 0; width: 100%; height: 48px; background: var(--leaf);
    display: flex; align-items: center; justify-content: center;
  }
  .business-card .contact { font-size: 6.5px; }

  /* Compliment slip */
  .compliment-slip { left: 72px; top: 372px; width: 496px; height: 231px; }
  .header-band { position: absolute; left: 0; top: 0; width: 100%; background: var(--leaf); display: flex; }
  .header-band .logo-panel { background: var(--paper); display: flex; align-items: center; justify-content: center; flex: none; }
  .header-band .contact-area { flex: 1; display: flex; align-items: center; justify-content: center; }
  .compliment-slip .header-band { height: 61px; }
  .compliment-slip .logo-panel { width: 232px; }
  .compliment-slip .wordmark { font-size: 21px; }
  .compliment-slip .contact { font-size: 7px; }
  .compliment-slip .greeting {
    position: absolute; left: 12px; top: 73px;
    font-size: 21px; font-weight: 400; color: var(--leaf);
  }
  .ghost-name {
    position: absolute; color: var(--ghost); font-weight: 600; line-height: 1; white-space: nowrap;
  }
  .compliment-slip .ghost-name { left: 150px; top: 110px; font-size: 56px; }
  .foot-band { position: absolute; left: 0; bottom: 0; width: 100%; background: var(--forest); }
  .compliment-slip .foot-band { height: 16px; }

  /* Letterhead */
  .letterhead { left: 657px; top: 20px; width: 496px; height: 700px; }
  .letterhead .header-band { height: 60px; }
  .letterhead .logo-panel { width: 222px; }
  .letterhead .wordmark { font-size: 21px; }
  .letterhead .contact { font-size: 7px; }
  .letterhead .ghost-name { left: 40px; top: 300px; font-size: 84px; }
  .letterhead .foot-band { height: 27px; }

  /* Desktop wallpaper */
  .wallpaper { left: 280px; top: 740px; width: 704px; height: 439px; }
  .wallpaper .artwork {
    position: absolute; inset: 0;
    background: radial-gradient(ellipse at 50% 45%, var(--mist-2) 0%, var(--mist-1) 70%);
  }
  .wallpaper .wordmark {
    position: absolute; left: 0; right: 0; top: 190px;
    justify-content: center; font-size: 44px; gap: 12px;
  }
  .wallpaper .wordmark .mark-square { width: 26px; height: 26px; }
</style>
</head>
<body>
<main class="canvas">

  <section class="sheet business-card" aria-label="Business card">
    <div class="top-band"></div>
    <div class="wordmark"><span class="mark-square"></span>Copperfinch</div>
    <div class="person">
      <p class="person-name">Martin Keele</p>
      <p class="person-role">Company Director</p>
    </div>
    <div class="contact-band">
      <p class="contact">Phone: 01632 960418 &nbsp;email: hello@copperfinch.co.uk<br>17 harbour lane, Millbrook, County Down BT99 2QX</p>
    </div>
  </section>

  <section class="sheet compliment-slip" aria-label="Compliment slip">
    <div class="ghost-name" aria-hidden="true">Copperfinch</div>
    <header class="header-band">
      <div class="logo-panel"><div class="wordmark"><span class="mark-square"></span>Copperfinch</div></div>
      <div class="contact-area">
        <p class="contact">Phone: 01632 960418 &nbsp;email: hello@copperfinch.co.uk<br>17 harbour lane, Millbrook, County Down BT99 2QX</p>
      </div>
    </header>
    <p class="greeting">With Compliment....</p>
    <div class="foot-band"></div>
  </section>

  <section class="sheet letterhead" aria-label="A4 letterhead">
    <div class="ghost-name" aria-hidden="true">Copperfinch</div>
    <header class="header-band">
      <div class="logo-panel"><div class="wordmark"><span class="mark-square"></span>Copperfinch</div></div>
      <div class="contact-area">
        <p class="contact">Phone: 01632 960418 &nbsp;email: hello@copperfinch.co.uk<br>17 harbour lane, Millbrook, County Down BT99 2QX</p>
      </div>
    </header>
    <div class="foot-band"></div>
  </section>

  <section class="sheet wallpaper" aria-label="Desktop wallpaper">
    <div class="artwork" role="img" aria-label="Green botanical illustration of swirling vines, leaves and butterflies radiating from the centre on a pale textured background"></div>
    <div class="wordmark"><span class="mark-square"></span>Copperfinch Trading Limited</div>
  </section>

</main>
</body>
</html>
```